Brannigan Ashcroft LLC. custom built/handcrafted

I am recent small business owner looking to sell my art(drawings) and woodworking projects from my home. I have a very rough draft of a simple card design created on a simple digital program. I was hoping for a fancier lettering on the initial letters (BA). More of a calligraphy style. Also, the yellow border around the logo I would like to be a gold foil look. For it to be shiny or reflective look and to keep the other letters black with a consistent font on the card and the card white.

Target Market(s)

Local and neighboring cities

Industry/Entity Type

Art (drawing)/Woodworking

Contact Information for Business Card

My email tpashcroft@mailvane.net, phone number 949-517-3068. In the files provided it has a yellow border around the logo and I was looking to make that a gold foil.

Font styles to use
Serif
Decorative
Script

Requirements
Nice to have
• symbols for having a Facebook and Instagram

```html
<!DOCTYPE html>
<html lang="en">
<head>
<meta charset="utf-8">
<title>Brannigan Ashcroft LLC. — Business Card</title>
<link rel="stylesheet" href="https://fonts.googleapis.com/css2?family=Arimo&family=Libre+Caslon+Text&display=swap">
<style>
  :root {
    --backdrop: #e9e9e7;
    --card-white: #fbfbfa;
    --ink: #111111;
    --gold-line: #d9bf8c;
    --gold-deep: #a9812d;
    --gold-mid: #d6a84a;
    --gold-light: #f3e6a4;
    --gold-pale: #f8f0bd;
    --serif: "Libre Caslon Text", Georgia, serif;
    --sans: "Arimo", Arial, sans-serif;
  }
  html, body {
    margin: 0;
    width: 1200px;
    height: 801px;
    overflow: hidden;
    background: var(--backdrop);
  }
  .canvas {
    position: relative;
    width: 1200px;
    height: 801px;
    display: flex;
    align-items: center;
    justify-content: center;
    gap: 40px;
  }
  .card {
    position: relative;
    width: 540px;
    height: 309px;
    box-sizing: border-box;
    box-shadow: 0 6px 18px rgba(0,0,0,0.12);
  }

  /* Contact side */
  .card--contact {
    background: var(--card-white);
  }
  .contact__frame {
    position: absolute;
    inset: 22px;
    border: 3px solid var(--gold-line);
  }
  .contact__body {
    position: absolute;
    inset: 0;
    display: flex;
    align-items: center;
    justify-content: center;
    gap: 18px;
    padding-bottom: 14px;
  }
  .contact__identity {
    text-align: right;
  }
  .contact__name {
    font-family: var(--serif);
    font-size: 21px;
    letter-spacing: 0.5px;
    color: transparent;
    -webkit-text-stroke: 0.8px var(--ink);
    margin: 0;
    text-transform: uppercase;
  }
  .contact__role {
    font-family: var(--sans);
    font-size: 15px;
    color: var(--ink);
    margin: 2px 0 0;
    letter-spacing: 0.5px;
  }
  .contact__divider {
    width: 1.5px;
    height: 46px;
    background: var(--ink);
  }
  .contact__details {
    list-style: none;
    margin: 0;
    padding: 0;
    font-family: var(--sans);
    font-size: 15px;
    color: var(--ink);
  }
  .contact__details li {
    display: flex;
    align-items: center;
    gap: 8px;
    line-height: 22px;
  }
  .contact__icon { width: 13px; height: 13px; }
  .contact__social {
    position: absolute;
    left: 50%;
    bottom: 12px;
    transform: translateX(-50%);
    display: flex;
    gap: 8px;
    padding: 0 8px;
    background: var(--card-white);
  }
  .social-mark {
    width: 20px;
    height: 20px;
    border-radius: 5px;
    background: var(--ink);
  }

  /* Brand side */
  .card--brand {
    background:
      linear-gradient(100deg,
        var(--gold-deep) 0%,
        var(--gold-mid) 18%,
        var(--gold-pale) 38%,
        var(--gold-mid) 52%,
        var(--gold-light) 68%,
        var(--gold-mid) 85%,
        var(--gold-deep) 100%);
    display: flex;
    flex-direction: column;
    align-items: center;
    justify-content: center;
    gap: 14px;
  }
  .brand__frame {
    width: 320px;
    height: 150px;
    border: 2.5px solid var(--ink);
    display: flex;
    align-items: center;
    justify-content: center;
    box-sizing: border-box;
  }
  .brand__name {
    font-family: var(--serif);
    font-size: 20px;
    color: var(--ink);
    text-transform: uppercase;
    letter-spacing: 1px;
    text-align: center;
    line-height: 1.35;
    margin: 0;
  }
  .brand__tagline {
    font-family: var(--serif);
    font-size: 12px;
    color: var(--ink);
    letter-spacing: 0.6px;
    text-transform: uppercase;
    margin: 0;
  }
</style>
</head>
<body>
<main class="canvas">

  <section class="card card--contact" aria-label="Business card contact side">
    <div class="contact__frame"></div>
    <div class="contact__body">
      <div class="contact__identity">
        <p class="contact__name">Tobias P. Ashcroft</p>
        <p class="contact__role">OWNER</p>
      </div>
      <div class="contact__divider"></div>
      <ul class="contact__details">
        <li>
          <svg class="contact__icon" viewBox="0 0 16 16" aria-hidden="true">
            <path d="M4 1.5l2.2 3-1.3 1.6c.8 1.9 2.3 3.4 4.2 4.2l1.6-1.3 3 2.2-1.2 2.6C6.8 13.6 2.4 9.2 1.5 3.5z" fill="#111"/>
          </svg>
          949-517-3068
        </li>
        <li>
          <svg class="contact__icon" viewBox="0 0 16 16" aria-hidden="true">
            <rect x="1.5" y="3.5" width="13" height="9" fill="none" stroke="#111" stroke-width="1.4"/>
            <path d="M1.5 3.5l6.5 5 6.5-5" fill="none" stroke="#111" stroke-width="1.4"/>
          </svg>
          tpashcroft@mailvane.net
        </li>
      </ul>
    </div>
    <div class="contact__social" aria-label="Social media profiles">
      <span class="social-mark"></span>
      <span class="social-mark"></span>
    </div>
  </section>

  <section class="card card--brand" aria-label="Business card gold foil brand side">
    <div class="brand__frame">
      <p class="brand__name">Brannigan Ashcroft</p>
    </div>
    <p class="brand__tagline">Custom Built · Handcrafted</p>
  </section>

</main>
</body>
</html>
```